Play on Words (French Puns)

Cover (11 x 17.8 cm) for a book of French plays on words. (Author: "Mathis Doreau" Title: "The Tumblers" Subtitle "Letter Puzzles To Nibble" Publisher (at the bottom of the page): "Quill Editions"

Target Market(s)

General public

Industry/Entity Type

Book Publisher

Colors

Designer to choose colors to be used in the design.

Requirements
Must have
• "Unserious" look
Should not have
• Eiffel Tower, triumphal arch (it's a book on French language, not on France)

```html
<!DOCTYPE html>
<html lang="en">
<head>
<meta charset="utf-8">
<title>The Tumblers — Mathis Doreau</title>
<link rel="stylesheet" href="https://fonts.googleapis.com/css2?family=Rubik:wght@800&family=Fredoka:wght@700&family=Open+Sans:wght@300&display=swap">
<style>
  :root {
    --paper: #ffffff;
    --ink: #0a0a0a;
    --ink-soft: #333333;
    --outline: #1a1a2a;
    --violet: #4a45dc;
    --blue: #1f78e6;
    --purple: #8c2fae;
    --teal: #1d8c8c;
    --red: #e01a1a;
    --yellow: #f5cf2e;
    --green: #55b832;
    --lime: #98bb14;
    --figure-skin: #f5b8a8;
    --figure-shirt: #6cbf4a;
    --figure-jeans: #4a7ac8;
  }
  * { margin: 0; padding: 0; box-sizing: border-box; }
  html, body { width: 880px; height: 1200px; overflow: hidden; background: var(--paper); }
  .cover { position: relative; width: 880px; height: 1200px; background: var(--paper); }
  .author {
    position: absolute; left: 36px; top: 58px;
    font-family: "Rubik", sans-serif; font-weight: 800;
    font-size: 52px; color: var(--ink); letter-spacing: 0.2px;
  }
  .title {
    font-family: "Fredoka", sans-serif; font-weight: 700;
    line-height: 1; text-transform: uppercase;
  }
  .title-line { position: absolute; left: 34px; white-space: nowrap; }
  .title-line--first { top: 170px; font-size: 168px; letter-spacing: -4px; }
  .title-line--second { top: 360px; font-size: 150px; letter-spacing: -5px; }
  .letter {
    display: inline-block;
    text-shadow: 3px 4px 0 var(--outline);
  }
  .letter--tilt-l { transform: rotate(-5deg); }
  .letter--tilt-r { transform: rotate(5deg); }
  .letter--drop { transform: translateY(8px); }
  .c-violet { color: var(--violet); }
  .c-blue { color: var(--blue); }
  .c-purple { color: var(--purple); }
  .c-teal { color: var(--teal); }
  .c-red { color: var(--red); }
  .c-yellow { color: var(--yellow); }
  .c-green { color: var(--green); }
  .c-lime { color: var(--lime); }
  .subtitle {
    position: absolute; left: 37px; top: 584px;
    font-family: "Rubik", sans-serif; font-weight: 800;
    font-size: 32px; color: var(--ink);
  }
  .figure-art {
    position: absolute; left: 308px; top: 724px; width: 264px; height: 308px;
    border-radius: 40% 40% 30% 30%;
    background: linear-gradient(180deg, var(--figure-skin) 0%, var(--figure-skin) 45%, var(--figure-shirt) 65%, var(--figure-jeans) 100%);
  }
  .publisher {
    position: absolute; left: 0; right: 0; top: 1136px; text-align: center;
    font-family: "Open Sans", sans-serif; font-weight: 300;
    font-size: 25px; color: var(--ink-soft);
  }
</style>
</head>
<body>
  <main class="cover">
    <h2 class="author">Mathis Doreau</h2>
    <h1 class="title">
      <span class="title-line title-line--first"><span class="letter c-violet letter--tilt-l">T</span><span class="letter c-blue letter--drop">H</span><span class="letter c-purple letter--tilt-r">E</span></span>
      <span class="title-line title-line--second"> <span class="letter c-teal letter--tilt-l">T</span><span class="letter c-red letter--drop">U</span><span class="letter c-yellow letter--tilt-r">M</span><span class="letter c-green">B</span><span class="letter c-red letter--tilt-l">L</span><span class="letter c-lime letter--drop">E</span><span class="letter c-yellow letter--tilt-r">R</span><span class="letter c-green letter--tilt-l">S</span></span>
    </h1>
    <p class="subtitle">Letter Puzzles To Nibble</p>
    <div class="figure-art" role="img" aria-label="Cartoon illustration of a laughing man in a green shirt and blue jeans"></div>
    <p class="publisher">Quill Editions</p>
  </main>
</body>
</html>
```